Criação de Manual da Marca para Marketing & Comunicação
A empresa queria:
" Vamos iniciar atividade em junho. Incialmente, eugência com prestadores terceirizados, venda via network, em seguida tráfego pago e orgânico. Pretendo terceirizar a produção de criativos e vídeos. "

```html
<!DOCTYPE html>
<html lang="pt-BR">
<head>
<meta charset="UTF-8">
<title>Manual da Marca — Marca Principal</title>
<link href="https://fonts.googleapis.com/css2?family=Montserrat:wght@400;500;700&display=swap" rel="stylesheet">
<style>
  :root {
    --canvas: #ffffff;
    --page: #ffffff;
    --panel: #202328;
    --panel-text: #d9dbde;
    --heading-light: #ffffff;
    --ink: #1c1d20;
    --muted: #6b6e73;
    --rule: #c9cbce;
    --accent: #ffffff;
  }
  * { margin: 0; padding: 0; box-sizing: border-box; }
  html, body {
    width: 1200px; height: 1200px; overflow: hidden;
    background: var(--canvas);
    font-family: "Montserrat", sans-serif;
  }
  .spread {
    position: absolute; left: 0; top: 288px;
    width: 1200px; height: 620px;
    background: var(--page);
    box-shadow: 0 2px 14px rgba(0,0,0,0.12);
  }
  .sidebar {
    position: absolute; left: 0; top: 0;
    width: 312px; height: 100%;
    background: var(--panel);
    color: var(--panel-text);
    padding: 84px 38px 0 70px;
  }
  .sidebar h2 {
    font-size: 19px; font-weight: 700; color: var(--heading-light);
    margin-bottom: 12px;
  }
  .sidebar p {
    font-size: 10.5px; line-height: 1.55; margin-bottom: 12px;
  }
  .sidebar-mark {
    position: absolute; left: 70px; top: 470px;
    display: flex; align-items: center; gap: 12px;
  }
  .mark-square {
    width: 34px; height: 34px; border: 3px solid var(--accent);
  }
  .mark-name {
    font-size: 22px; font-weight: 700; color: var(--accent); letter-spacing: 1px;
    line-height: 1;
  }
  .mark-name small { display: block; font-size: 22px; }

  .version-label {
    position: absolute; left: 336px; top: 290px;
    font-size: 9px; color: var(--muted); letter-spacing: 0.5px;
  }
  .logo-frame {
    position: absolute; left: 408px; top: 324px;
    width: 396px; height: 108px;
    border: 1px solid var(--rule);
  }
  .logo-frame .symbol-zone {
    position: absolute; left: 0; top: 0; width: 92px; height: 100%;
    border-right: 1px solid var(--rule);
    display: flex; align-items: center; justify-content: center;
  }
  .symbol-label {
    position: absolute; left: 12px; top: 24px;
    font-size: 8.5px; color: var(--muted); letter-spacing: 0.5px;
  }
  .logo-square { width: 40px; height: 40px; background: var(--ink); margin-top: 14px; }
  .logo-word {
    position: absolute; left: 110px; top: 28px;
    font-size: 34px; font-weight: 700; color: var(--ink); line-height: 1.05;
    letter-spacing: 0.5px;
  }
  .logo-note {
    position: absolute; left: 322px; top: 44px; width: 66px;
    font-size: 7px; color: var(--muted); line-height: 1.3;
    border-left: 1px solid var(--rule); padding-left: 6px;
  }
  .description {
    position: absolute; left: 936px; top: 216px; width: 210px;
    font-size: 10.5px; line-height: 1.5; color: var(--ink);
  }
  .description p { margin-bottom: 12px; }
  .page-number {
    position: absolute; right: 34px; bottom: 22px;
    font-size: 10px; font-weight: 700; color: var(--ink);
  }
</style>
</head>
<body>
  <main class="spread">
    <aside class="sidebar">
      <h2>Marca Principal</h2>
      <p>A logomarca é composta por elementos segmentados que formam a identidade visual da marca: Símbolo, Logotipo, Denominação e Tipografia.</p>
      <p>O símbolo pode ser usado separado como marca d'água, elemento visual ou em materiais gráficos da empresa. Na versão original, a logomarca pode ser impressa sem alterações de proporção na maioria dos métodos de impressão.</p>
      <p>Alguns métodos de impressão:</p>
      <p>Off-set, impressão digital, banner de impressão, silk screen, plotter de recorte, serigrafia, bordados, entre outros.</p>
      <div class="sidebar-mark">
        <span class="mark-square"></span>
        <span class="mark-name">VERTIX<small>MEDIA</small></span>
      </div>
    </aside>

    <span class="version-label">VERSÃO ÚNICA</span>
    <div class="logo-frame">
      <div class="symbol-zone">
        <span class="symbol-label">SÍMBOLO</span>
        <span class="logo-square"></span>
      </div>
      <span class="logo-word">VERTIX<br>MEDIA</span>
      <span class="logo-note">LOGOTIPO COMPOSTO PELO NOME</span>
    </div>

    <section class="description">
      <p>Nosso logotipo é o principal componente de nossa identidade, o principal elemento visual que nos identifica.</p>
      <p>A assinatura é uma combinação do próprio símbolo e o nome da empresa, eles têm um relacionamento fixo que nunca deve ser alterado de forma alguma.</p>
      <p>O logotipo Vertix Media possui apenas uma versão de orientação - horizontal.</p>
    </section>

    <span class="page-number">04</span>
  </main>
</body>
</html>
```